Business Card Design

We Need a business card design for my company based in Tv Radio and music Productions and hunt Talent.

Industry/Entity Type

Business

Contact Information for Business Card

BrentaVue Production's, Teodor Vignoles,Cell Phone 318 4957310
Musician, Productor, Hunt Talent. Miami Fla. www.brentavue.net Mail. teodorvignoles@mailvana.com

```html
<!DOCTYPE html>
<html lang="en">
<head>
<meta charset="utf-8">
<title>BrentaVue Production's – Business Card</title>
<link rel="stylesheet" href="https://fonts.googleapis.com/css2?family=Lobster&family=Montserrat:wght@400;700&display=swap">
<style>
  :root {
    --card-yellow: #f8d51e;
    --card-yellow-light: #fbe04a;
    --card-yellow-deep: #efc417;
    --ink-black: #111111;
    --band-orange: #f28f1c;
    --band-blue: #1f7bc3;
    --band-green: #2fb04b;
    --text-white: #ffffff;
    --emblem-ink: rgba(150, 115, 30, 0.2);
  }
  html, body {
    margin: 0;
    padding: 0;
    overflow: hidden;
    background: #ffffff;
  }
  .card {
    position: relative;
    width: 1200px;
    height: 703px;
    overflow: hidden;
    background: var(--card-yellow);
    font-family: "Montserrat", Arial, sans-serif;
  }
  .star-field {
    position: absolute;
    inset: 0;
    background:
      radial-gradient(ellipse at 30% 30%, var(--card-yellow-light) 0%, rgba(251, 224, 74, 0) 55%),
      radial-gradient(ellipse at 75% 80%, var(--card-yellow-light) 0%, rgba(251, 224, 74, 0) 50%),
      linear-gradient(160deg, var(--card-yellow) 0%, var(--card-yellow-deep) 100%);
  }
  .emblem-mark {
    position: absolute;
    left: 250px;
    top: 300px;
    display: flex;
    align-items: center;
    gap: 22px;
  }
  .emblem-square {
    width: 70px;
    height: 70px;
    background: var(--emblem-ink);
  }
  .emblem-name {
    font-family: "Montserrat", Arial, sans-serif;
    font-weight: 700;
    font-size: 64px;
    color: var(--emblem-ink);
    white-space: nowrap;
  }
  .company-name {
    position: absolute;
    left: 190px;
    top: 118px;
    margin: 0;
    font-family: "Lobster", cursive;
    font-weight: 400;
    font-size: 90px;
    line-height: 1;
    color: var(--ink-black);
    transform: rotate(-6deg);
    transform-origin: left center;
    white-space: nowrap;
  }
  .band {
    position: absolute;
    display: flex;
    align-items: center;
    box-sizing: border-box;
    color: var(--text-white);
    white-space: nowrap;
    box-shadow: 4px 6px 0 rgba(0, 0, 0, 0.12);
  }
  .band-name {
    left: 532px;
    top: 272px;
    width: 602px;
    height: 88px;
    background: var(--band-orange);
    transform: rotate(-2deg);
    padding-left: 50px;
    font-weight: 700;
    font-size: 44px;
    letter-spacing: 2px;
    text-transform: uppercase;
  }
  .band-phone {
    left: 624px;
    top: 380px;
    width: 524px;
    height: 80px;
    background: var(--band-blue);
    padding-left: 44px;
    font-weight: 400;
    font-size: 40px;
    gap: 22px;
  }
  .band-mail {
    left: 546px;
    top: 472px;
    width: 642px;
    height: 68px;
    background: var(--band-green);
    transform: rotate(-2deg);
    padding-left: 38px;
    font-weight: 400;
    font-size: 32px;
    gap: 18px;
  }
  .icon { flex: none; fill: var(--text-white); }
</style>
</head>
<body>
  <main class="card">
    <div class="star-field" role="img" aria-label="Yellow background scattered with light stars"></div>

    <div class="emblem-mark" aria-hidden="true">
      <div class="emblem-square"></div>
      <div class="emblem-name">BrentaVue</div>
    </div>

    <h1 class="company-name">BrentaVue Production's,</h1>

    <div class="band band-name">Teodor Vignoles</div>

    <div class="band band-phone">
      <svg class="icon" width="34" height="34" viewBox="0 0 24 24" aria-hidden="true">
        <path d="M6.6 10.8c1.4 2.8 3.8 5.1 6.6 6.6l2.2-2.2c.3-.3.7-.4 1-.2 1.1.4 2.3.6 3.6.6.6 0 1 .4 1 1V20c0 .6-.4 1-1 1C10.6 21 3 13.4 3 4c0-.6.4-1 1-1h3.5c.6 0 1 .4 1 1 0 1.3.2 2.5.6 3.6.1.3 0 .7-.2 1z"/>
      </svg>
      <span class="phone-number">318 4957310</span>
    </div>

    <div class="band band-mail">
      <svg class="icon" width="36" height="28" viewBox="0 0 24 18" aria-hidden="true">
        <path d="M0 1.5L12 9 24 1.5V0H0z"/>
        <path d="M0 4v14h24V4l-12 7.5z"/>
      </svg>
      <span class="email">teodorvignoles@mailvana.com</span>
    </div>
  </main>
</body>
</html>
```